TALVENTO needs a Sleek, Professional and Serious Web Design, this web design is aiming to be famous!

Dear Designers,

We need a web design for a new company based on the Internet named "talvento". I have already worked with PX to get my logo and it has been a wonderful experience which I want to repeat. We are kind of work social network, the web page will be mostly used to write comments on businesses around the world to help workers find which company fit the best for them. This website is also here to help people finding work by giving them the tools to make the right research.

For contents inspiration, you could see on the added files a sketch of the website but I am not asking you following it because it was just for giving the contents.

We do not have any example regarding website that we do like because all are coming so generic. We would like a very sleek website, where surfing become very intuitive and ergonomic (Brindlepost is not very ergonomic for example from our point of view). The website must reflect professionalism and seriousness and worker, world connexion.

We will be pleased to accept original designs as long as they fit to our requirements and if it is properly made of course: e.g. web page looking like a newspaper etc.

About colours, we are not decided yet but we are aiming a light orange (pastel style) or dark bluish green. Also, it comes to our attention that a web site mostly realized in grey-scale will be very interesting (touch of colour will be accepted as well if it miss too much dynamism) .

We will give the feedback as soon as possible because we would like to have 5 pages but it will be only very small changes on the next ones. (like adding 4 buttons)

Target Market(s)

Our target is relatively large because it is all people of working age, in numbers we can say a range of people aged from 18 to 45 years.

Industry/Entity Type

Internet

Number of Pages Required

3 page

Font styles to use
Sans Serif

Requirements
Must have
• Elements that must be on the web page are exposed below:
• - company logo ( .ai & .eps files on added files)
• - 4 buttons (Searcher "highlighted" / Advises / Jobs / Solutions)
• - login/account window
• - language button (e.g. a flag)
• - Window companies searcher (the most important, refer to the sketch)
• - classic menu down the page - about us / contact us / conditions / site map / community / politics / publicity / languages / copyright etc.
Nice to have
• We want a professional and serious website.
Should not have
• If you have a doubt, just ask us because nothing are coming to our mind.

```html
<!DOCTYPE html>
<html lang="en">
<head>
<meta charset="utf-8">
<title>Talvento – Company Searcher</title>
<link href="https://fonts.googleapis.com/css2?family=Oswald:wght@400;500;700&family=Open+Sans:ital,wght@0,400;0,600;0,700;1,400&display=swap" rel="stylesheet">
<style>
:root{
  --orange:#f7941d;
  --orange-light:#fda53a;
  --orange-dark:#f27a0e;
  --ink:#2b2b2b;
  --panel:#151515;
  --grey-text:#8e8e8e;
  --foot-bg:#ebeae8;
  --foot-link:#7c7c7c;
  --nav-text:#5a3208;
  --white:#fff;
}
*{box-sizing:border-box;margin:0;padding:0}
html,body{width:1016px;height:1200px;overflow:hidden;background:var(--white)}
body{position:relative;font-family:'Open Sans',sans-serif;color:var(--ink)}
.abs{position:absolute}

/* header */
.site-header{position:absolute;left:0;top:0;width:1016px;height:85px;
  background:linear-gradient(#fba03c,#f7931c);border-top:3px solid #4a4a4a;
  box-shadow:0 2px 4px rgba(0,0,0,.25);z-index:2}
.brand{position:absolute;left:104px;top:20px;display:flex;align-items:center;gap:6px}
.brand-dot{width:18px;height:18px;border-radius:50%;background:var(--ink)}
.brand-name{font-family:'Oswald',sans-serif;font-weight:700;font-size:31px;color:var(--ink);line-height:1;letter-spacing:.5px}
.main-nav{font-family:'Oswald',sans-serif;font-size:12px;text-transform:uppercase}
.main-nav a{position:absolute;top:34px;color:var(--nav-text);text-decoration:none;line-height:14px}
.main-nav a.active{top:27px;left:308px;width:59px;height:28px;line-height:28px;text-align:center;background:var(--ink);color:var(--white)}
.lang{position:absolute;left:782px;top:34px;display:flex;align-items:center;gap:4px;color:var(--nav-text);line-height:14px}
.account{position:absolute;left:825px;top:23px;width:98px;height:34px;background:var(--ink);color:var(--white);
  font-family:'Oswald',sans-serif;font-size:12px;text-align:center;line-height:34px}

/* hero */
.hero{position:absolute;left:0;top:85px;width:1016px;height:459px;background:#fafafa;border-bottom:1px solid #ddd}
.hero-photo{position:absolute;right:0;top:0;width:640px;height:458px;
  background:linear-gradient(100deg,#f6f4f2 0%,#e9dcd2 35%,#5e6270 55%,#2f3440 68%,#d8b9a0 82%,#f1ebe6 100%);
  -webkit-mask-image:linear-gradient(90deg,transparent,#000 35%);mask-image:linear-gradient(90deg,transparent,#000 35%)}
.searcher{position:absolute;left:93px;top:126px;width:373px;height:227px;background:var(--panel);padding:16px 17px}
.searcher h1{font-family:'Oswald',sans-serif;font-weight:700;font-size:33px;color:var(--white);line-height:1.1}
.searcher p{font-style:italic;font-size:12.5px;color:#8a8a8a;margin:6px 0 9px}
.row{display:flex;gap:8px;margin-bottom:9px}
.field{flex:1;height:30px;background:var(--white);font-style:italic;font-size:10.5px;color:#777;padding:8px 7px}
.btn-search{display:inline-block;margin-top:5px;background:linear-gradient(var(--orange-light),var(--orange-dark));
  color:var(--white);font-family:'Oswald',sans-serif;font-size:17px;padding:5px 23px;border-radius:2px}

/* what we do */
.intro{position:absolute;left:0;top:562px;width:1016px;text-align:center}
.intro h2{font-family:'Oswald',sans-serif;font-weight:400;font-size:29px;color:var(--ink)}
.intro p{width:670px;margin:8px auto 0;font-style:italic;font-size:12px;line-height:19px;color:var(--grey-text)}
.service{position:absolute;top:666px;width:240px;text-align:center}
.service .badge{width:76px;height:76px;border-radius:50%;background:var(--orange);margin:0 auto;display:flex;align-items:center;justify-content:center}
.service .badge.dark{background:var(--ink)}
.service h3{font-family:'Oswald',sans-serif;font-weight:400;font-size:17px;margin-top:16px;color:var(--ink)}
.service h3.hl{color:var(--orange)}
.service p{font-style:italic;font-size:11px;line-height:17px;color:var(--grey-text);margin-top:8px}

/* footer */
.site-footer{position:absolute;left:0;top:869px;width:1016px;height:278px;background:var(--foot-bg);border-top:1px solid #d6d6d6}
.col{position:absolute;top:22px}
.col h4{font-family:'Oswald',sans-serif;font-weight:400;font-size:17px;color:#444;margin-bottom:6px}
.col a{display:block;font-size:11px;line-height:17px;color:var(--foot-link);text-decoration:none}
.newsletter .email{display:inline-block;width:203px;height:26px;background:var(--white);border-radius:13px;font-style:italic;font-size:10px;color:#777;padding:6px 11px;box-shadow:inset 0 1px 2px rgba(0,0,0,.15)}
.newsletter .sub{display:inline-block;margin-left:5px;height:26px;background:var(--orange);color:var(--white);font-size:11.5px;border-radius:13px;padding:5px 14px;vertical-align:top}
.newsletter small{display:block;font-size:8.5px;color:#777;margin-top:6px}
.social{display:flex;gap:17px;margin-top:11px;font-family:'Oswald',sans-serif;font-size:12.5px;color:#666}
.social span{display:flex;align-items:center;gap:6px}
.social i{width:17px;height:17px;border-radius:50%;background:#aaa;display:block}
.ad-space{position:absolute;left:108px;top:183px;width:616px;height:76px;
  background:linear-gradient(90deg,#f7a13a,#f58f1b)}
.foot-brand{position:absolute;left:757px;top:230px;display:flex;align-items:center;gap:6px}
.foot-brand .dot{width:14px;height:14px;border-radius:50%;background:#8a8a8a}
.foot-brand span{font-family:'Oswald',sans-serif;font-weight:700;font-size:26px;color:#8a8a8a;line-height:1}
.bottom-bar{position:absolute;left:0;top:1147px;width:1016px;height:53px;background:#f2f2f2;border-top:1px solid #ddd;
  font-size:11px;color:#777}
.bottom-bar .copy{position:absolute;left:114px;top:17px}
.bottom-bar nav{position:absolute;right:108px;top:17px}
.bottom-bar nav a{color:#777;text-decoration:none}
.bottom-bar nav em{font-style:normal;margin:0 5px}
</style>
</head>
<body>

<header class="site-header">
  <div class="brand"><span class="brand-dot"></span><span class="brand-name">TALVENTO</span></div>
  <nav class="main-nav">
    <a class="active" href="#">Home</a>
    <a href="#" style="left:375px">Company</a>
    <a href="#" style="left:445px">Advises</a>
    <a href="#" style="left:508px">Jobs</a>
    <a href="#" style="left:555px">Solutions</a>
    <a href="#" style="left:632px">About Us</a>
    <a href="#" style="left:704px">Contact Us</a>
    <span class="lang">
      <svg width="12" height="8" viewBox="0 0 12 8"><rect width="12" height="8" fill="#c8102e"/><rect y="1.2" width="12" height="1.1" fill="#fff"/><rect y="3.5" width="12" height="1.1" fill="#fff"/><rect y="5.8" width="12" height="1.1" fill="#fff"/><rect width="5" height="4.3" fill="#2a3f8f"/></svg>EN
    </span>
  </nav>
  <div class="account">LOGIN &nbsp;|&nbsp; SIGN UP</div>
</header>

<section class="hero">
  <div class="hero-photo" role="img" aria-label="Photo of two business colleagues reviewing a tablet together at an office desk"></div>
  <form class="searcher">
    <h1>COMPANY SEARCHER</h1>
    <p>Lorem ipsum dolor sit amet consectetur adipscing elit,</p>
    <div class="row"><div class="field">Company Name..</div><div class="field">VAT Number..</div></div>
    <div class="row"><div class="field">City</div><div class="field">Post Code</div><div class="field">Country</div></div>
    <span class="btn-search">Search Now</span>
  </form>
</section>

<section class="intro">
  <h2>What We Do?</h2>
  <p>Lorem ipsum dolor sit amet, consectetur adipiscing elit, sed do eiusmod tempor incididunt ut labore et dolore magna aliqua. Ut enim ad minim veniam, quis nostrud laboris nisi ut aliquip ex ea commodo consequat..</p>
</section>

<svg class="abs" style="left:320px;top:680px" width="100" height="24" viewBox="0 0 100 24"><path d="M2 20 Q45 -2 92 16" fill="none" stroke="#ccc" stroke-width="2" stroke-dasharray="4 4"/><path d="M86 8 L98 20 L84 20 Z" fill="#ccc"/></svg>
<svg class="abs" style="left:596px;top:680px" width="100" height="24" viewBox="0 0 100 24"><path d="M2 20 Q45 -2 92 16" fill="none" stroke="#ccc" stroke-width="2" stroke-dasharray="4 4"/><path d="M86 8 L98 20 L84 20 Z" fill="#ccc"/></svg>

<div class="service" style="left:113px">
  <div class="badge"><svg width="40" height="40" viewBox="0 0 40 40"><circle cx="14" cy="17" r="5" fill="#fff"/><path d="M4 36 Q4 24 14 24 Q24 24 24 36Z" fill="#fff"/><rect x="20" y="4" width="16" height="11" rx="5" fill="none" stroke="#fff" stroke-width="2"/></svg></div>
  <h3>TALVENTO ADVISES</h3>
  <p>Lorem ipsum dolor sit amet, consectetur adipiscing elit, sed do eiusmod tempor incidid-unt ut labore et dolore magna aliqua.</p>
</div>
<div class="service" style="left:388px">
  <div class="badge dark"><svg width="40" height="40" viewBox="0 0 40 40"><rect x="9" y="10" width="20" height="24" rx="2" fill="#fff" transform="rotate(-12 19 22)"/><path d="M13 18h11M13 23h11M13 28h8" stroke="#2b2b2b" stroke-width="2" transform="rotate(-12 19 22)"/></svg></div>
  <h3 class="hl">TALVENTO JOBS</h3>
  <p>Lorem ipsum dolor sit amet, consectetur adipiscing elit, sed do eiusmod tempor incidid-unt ut labore et dolore magna aliqua.</p>
</div>
<div class="service" style="left:663px">
  <div class="badge"><svg width="40" height="40" viewBox="0 0 40 40"><circle cx="20" cy="18" r="8" fill="#fff"/><rect x="16" y="25" width="8" height="7" rx="1" fill="#fff"/><path d="M20 3v4M8 8l3 3M32 8l-3 3M4 18h4M32 18h4" stroke="#fff" stroke-width="2" stroke-linecap="round"/></svg></div>
  <h3>TALVENTO SOLUTIONS</h3>
  <p>Lorem ipsum dolor sit amet, consectetur adipiscing elit, sed do eiusmod tempor incidid-unt ut labore et dolore magna aliqua.</p>
</div>

<footer class="site-footer">
  <div class="col" style="left:108px"><h4>Site Links</h4><a>Home</a><a>Company</a><a>Advises</a><a>Jobs</a><a>Solutions</a><a>About Us</a><a>Contact Us</a></div>
  <div class="col" style="left:232px"><h4>About Us</h4><a>Lorem ipsum</a><a>Dolor Sit</a><a>Amet</a><a>Consectetur</a><a>Adipsicing Elit</a></div>
  <div class="col" style="left:364px"><h4>Services</h4><a>Lorem ipsum</a><a>Dolor Sit Amet</a><a>Consectetur</a><a>Adipsicing Elit</a></div>
  <div class="col" style="left:488px"><h4>Contact Us</h4><a>Lorem ipsum</a><a>Dolor Sit</a><a>Amet</a><a>Consectetur</a><a>Adipsicing Elit</a></div>
  <div class="col newsletter" style="left:619px"><h4>Subscribe To Our Newsletter</h4>
    <span class="email">Your Email Address</span><span class="sub">Subscribe</span>
    <small>You'll get an email about once a month. we'll never share your address</small>
    <div class="social"><span><i></i>Brindlepost</span><span><i></i>Chirpline</span><span><i></i>Email</span><span><i></i>Pinwell</span></div>
  </div>
  <div class="ad-space" role="img" aria-label="Advertising banner space for a partner promotion"></div>
  <div class="foot-brand"><span class="dot"></span><span>TALVENTO</span></div>
</footer>

<div class="bottom-bar">
  <span class="copy">Copyright © 2015 talvento.com - All Rights Reserved</span>
  <nav><a>About us</a><em>|</em><a>Contact us</a><em>|</em><a>Community</a><em>|</em><a>Publicity</a><em>|</em><a>Conditions</a><em>|</em><a>Politics</a><em>|</em><a>Language</a></nav>
</div>

</body>
</html>
```